I need a business card for myself, being a proprietor of a funeral parlor based in Manila. I'd like the card to have either of the following:
White Font on Black Background
or
Black Font on White Background
No logo is needed however I will appreciate any efforts to show a symbol of eternal happiness, aptly designed with above mentioned colors in mind.
Company name, address and contact on the lower right corner.
Logo or symbol anywhere.
Quillstone Funeral Services
+639174826351
darvik4521@pelmora.com
corner of Brisco Avenue and Velhurst Street
Makati City, Philippines
Thank you.
Update: Please include a small dove in your design. You are free to choose where you would like it on the card.

```html
<!DOCTYPE html>
<html lang="en">
<head>
<meta charset="utf-8">
<title>Quillstone Funeral Services — Business Card</title>
<link rel="stylesheet" href="https://fonts.googleapis.com/css2?family=Arimo:wght@700&family=Jost:wght@300&display=swap">
<style>
  :root {
    --card-bg: #0a0a0a;
    --ink: #ffffff;
  }
  html, body {
    margin: 0;
    padding: 0;
    overflow: hidden;
    background: var(--card-bg);
  }
  .card {
    position: relative;
    width: 1200px;
    height: 686px;
    background: var(--card-bg);
    color: var(--ink);
    overflow: hidden;
  }
  .brand-mark {
    position: absolute;
    left: 114px;
    top: 120px;
    width: 432px;
    height: 266px;
    display: flex;
    flex-direction: column;
    align-items: center;
    justify-content: center;
    gap: 26px;
  }
  .brand-mark__circle {
    width: 120px;
    height: 120px;
    border-radius: 50%;
    border: 3px solid var(--ink);
    box-sizing: border-box;
  }
  .brand-mark__name {
    font-family: "Jost", "Futura", sans-serif;
    font-weight: 300;
    font-size: 40px;
    line-height: 1;
    letter-spacing: 2px;
    color: var(--ink);
  }
  .contact {
    position: absolute;
    left: 690px;
    top: 468px;
  }
  .contact__company {
    margin: 0 0 14px;
    font-family: "Arimo", "Helvetica Neue", Arial, sans-serif;
    font-weight: 700;
    font-size: 30px;
    line-height: 1.2;
    letter-spacing: 0.2px;
  }
  .contact__line {
    margin: 0;
    font-family: "Jost", "Futura", sans-serif;
    font-weight: 300;
    font-size: 26px;
    line-height: 34.5px;
    letter-spacing: 0;
    white-space: nowrap;
  }
</style>
</head>
<body>
  <main class="card">
    <div class="brand-mark">
      <span class="brand-mark__circle"></span>
      <span class="brand-mark__name">Quillstone</span>
    </div>

    <section class="contact">
      <h1 class="contact__company">Quillstone Funeral Services</h1>
      <p class="contact__line">+639174826351</p>
      <p class="contact__line">darvik4521@pelmora.com</p>
      <p class="contact__line">corner of Brisco Avenue and Velhurst Street</p>
      <p class="contact__line">Makati City, Philippines</p>
    </section>
  </main>
</body>
</html>
```